Brightwave Business Card

Professional Business Card Design required using the attached contact information.

Contact information can be rearranged as required.

The company is a new start up venture developing solar systems, the branding should be in keeping with that of one of the investors whose website is as follows https://www.quorvex.com/

```html
<!DOCTYPE html>
<html lang="en">
<head>
<meta charset="utf-8">
<title>Brightwave Renewables – Business Card</title>
<link href="https://fonts.googleapis.com/css2?family=Michroma&family=Montserrat:wght@600&family=Roboto:wght@300&family=Roboto+Condensed:wght@400&display=swap" rel="stylesheet">
<style>
  :root {
    --backdrop: #e6e7e8;
    --paper: #ffffff;
    --ink: #111416;
    --night: #050607;
    --pine: #2a6653;
    --pine-bright: #2f7a60;
    --sky-dot: #5b93b3;
    --light-text: #f2f2f2;
  }
  * { box-sizing: border-box; margin: 0; padding: 0; }
  html, body { width: 1200px; height: 965px; overflow: hidden; background: var(--backdrop); }
  .sheet {
    width: 1200px; height: 965px;
    display: flex; flex-direction: column; align-items: center; justify-content: center; gap: 36px;
  }
  .card {
    width: 760px; height: 434px;
    position: relative; overflow: hidden;
    box-shadow: 0 10px 28px rgba(0,0,0,.22);
  }
  /* Front */
  .card-front {
    background: var(--paper);
    display: flex; align-items: center; justify-content: center; gap: 18px;
  }
  .brand-dot { width: 22px; height: 22px; border-radius: 50%; background: var(--pine); }
  .brand-name {
    font-family: "Montserrat", sans-serif; font-weight: 600;
    font-size: 40px; letter-spacing: 3px; color: var(--ink);
  }
  /* Back */
  .card-back { display: flex; }
  .back-panel { width: 41%; background: var(--pine); }
  .back-info {
    flex: 1; background: var(--night);
    padding: 58px 40px 0 38px; position: relative;
  }
  .holder-name {
    font-family: "Michroma", sans-serif; font-size: 27px; letter-spacing: 2px;
    color: var(--pine-bright); text-transform: uppercase; position: relative;
  }
  .holder-name::before {
    content: ""; position: absolute; left: -52px; top: 8px;
    width: 22px; height: 22px; border-radius: 50%; background: var(--sky-dot);
  }
  .company {
    font-family: "Roboto", sans-serif; font-weight: 300; font-size: 25px;
    color: var(--pine-bright); margin-top: 22px;
  }
  .contact-list {
    list-style: none; margin-top: 34px;
    font-family: "Roboto Condensed", sans-serif; font-size: 21px; color: var(--light-text);
    line-height: 1.25;
  }
  .contact-item { display: flex; align-items: flex-start; gap: 14px; margin-bottom: 22px; }
  .contact-item.tight { margin-bottom: 4px; }
  .contact-icon { width: 20px; height: 20px; flex: none; margin-top: 3px; }
</style>
</head>
<body>
<main class="sheet">
  <section class="card card-front" aria-label="Card front">
    <span class="brand-dot"></span>
    <span class="brand-name">BRIGHTWAVE RENEWABLES</span>
  </section>

  <section class="card card-back" aria-label="Card back">
    <div class="back-panel"></div>
    <div class="back-info">
      <h1 class="holder-name">Daniel Corrin</h1>
      <p class="company">Brightwave Renewables LLC</p>
      <ul class="contact-list">
        <li class="contact-item">
          <svg class="contact-icon" viewBox="0 0 20 20" fill="none" stroke="var(--pine-bright)" stroke-width="2"><path d="M10 19s-6-6.5-6-11a6 6 0 0 1 12 0c0 4.5-6 11-6 11z"/><circle cx="10" cy="8" r="2"/></svg>
          <span>318 Harbor Street<br>Salem, MA 01970</span>
        </li>
        <li class="contact-item tight">
          <svg class="contact-icon" viewBox="0 0 20 20" fill="none" stroke="var(--pine-bright)" stroke-width="2"><path d="M4 2h4l2 5-2.5 1.5a10 10 0 0 0 4 4L13 10l5 2v4a2 2 0 0 1-2 2A15 15 0 0 1 2 4a2 2 0 0 1 2-2z"/></svg>
          <span>+1 (555) 014-2763</span>
        </li>
        <li class="contact-item">
          <svg class="contact-icon" viewBox="0 0 20 20" fill="none" stroke="var(--pine-bright)" stroke-width="2"><rect x="2" y="4" width="16" height="12"/><path d="M2 4l8 7 8-7"/></svg>
          <span>daniel.corrin@brightwave-renewables.com</span>
        </li>
      </ul>
    </div>
  </section>
</main>
</body>
</html>
```